Velora Beauty Clinic

I need a web design for a Cosmetic Surgery Clinic. The current site is velora-beauty-clinic.example. The design should be:
- Flat Design with big banner
- Warm colors
- Responsive Layout
- SEO friendly

Cosmetic

```html
<!DOCTYPE html>
<html lang="en">
<head>
<meta charset="utf-8">
<title>Velora Beauty Clinic – Face, Body and Breast Plastic Surgery</title>
<link rel="stylesheet" href="https://fonts.googleapis.com/css2?family=Open+Sans:ital,wght@0,300;0,400;0,600;0,700;1,400&display=swap">
<style>
:root{
  --pink:#e5467f;
  --pink-dark:#c42a63;
  --pink-deep:#a81f52;
  --pink-soft:#f7d3e0;
  --ink:#333333;
  --muted:#666666;
  --grey-bg:#efefef;
  --dark:#2b2b2b;
  --white:#ffffff;
}
*{box-sizing:border-box;margin:0;padding:0}
html,body{width:1200px;height:4110px;overflow:hidden}
body{font-family:"Open Sans",Arial,sans-serif;color:var(--ink);background:var(--white);font-size:15px;line-height:1.6}
section,header,footer,nav{position:relative;width:1200px;overflow:hidden}
.btn{display:inline-block;padding:0 24px;height:44px;line-height:40px;font-size:14px;font-weight:600;letter-spacing:1px;text-transform:uppercase;border:2px solid var(--pink);color:var(--pink);background:transparent;white-space:nowrap}
.btn--solid{background:var(--pink);color:var(--white)}
.section-title{font-weight:300;text-transform:uppercase;letter-spacing:1px;color:var(--pink);font-size:30px;text-align:center}

/* header */
.site-header{height:115px;background:var(--pink-dark);color:var(--white)}
.brand{position:absolute;left:40px;top:36px;font-weight:700;font-size:38px;line-height:1;color:var(--white);letter-spacing:.5px}
.appointment{position:absolute;right:40px;top:30px;text-align:right}
.appointment small{display:block;font-size:14px;opacity:.9}
.appointment strong{font-size:28px;font-weight:400}

/* nav */
.main-nav{height:41px;background:var(--white);border-bottom:1px solid #e3e3e3}
.main-nav ul{list-style:none;display:flex;padding-left:40px}
.main-nav li{font-size:13px;font-weight:600;text-transform:uppercase;color:var(--muted);height:41px;line-height:41px;padding:0 27px}
.main-nav li.is-active{color:var(--pink);border-top:3px solid var(--pink);line-height:35px}

/* hero */
.hero{height:666px}
.hero-photo{position:absolute;inset:0;background:linear-gradient(180deg,#a9d8ee 0%,#6cc0d2 100%)}
.hero-caption{position:absolute;left:40px;top:210px;width:500px;padding:26px 28px;background:rgba(30,30,30,.78);color:var(--white)}
.hero-caption h1{font-size:24px;font-weight:700;color:var(--pink);letter-spacing:1px;text-transform:uppercase}
.hero-caption p{font-size:14px;margin:10px 0 18px;line-height:1.55}
.hero-caption .btn{height:36px;line-height:32px;font-size:12px;padding:0 16px;margin-right:8px}
.hero-dots{position:absolute;left:68px;top:440px;display:flex;gap:8px}
.dot{width:11px;height:11px;border-radius:50%;background:rgba(255,255,255,.6)}
.dot.is-active{background:var(--pink)}
.hero-arrow{position:absolute;top:300px;width:44px;height:44px}
.hero-arrow--prev{left:-12px}
.hero-arrow--next{right:-12px}

/* intro */
.intro{height:218px;text-align:center;padding-top:58px}
.intro p{width:860px;margin:16px auto 0;font-size:16px;color:var(--ink)}

/* experience */
.experience{height:550px;background:var(--grey-bg)}
.doctor-photo{position:absolute;left:150px;top:50px;width:300px;height:460px;background:linear-gradient(180deg,#e9ecef 0%,#cfd6dc 55%,#f7f7f7 100%)}
.experience-copy{position:absolute;left:620px;top:60px;width:520px}
.experience-copy h2{font-weight:300;font-size:30px;color:var(--pink);text-transform:uppercase;border-bottom:1px solid #d6d6d6;padding-bottom:8px;margin-bottom:16px}
.experience-copy p{font-size:14px;color:var(--muted);margin-bottom:14px}
.experience-copy .btn{margin-right:14px;margin-top:8px}

/* what we do */
.services{height:460px;background:var(--pink)}
.services .section-title{color:var(--white);padding-top:46px}
.service-grid{position:absolute;left:40px;top:120px;display:flex;gap:4px}
.service{width:277px}
.service-photo{height:270px}
.service-photo--face{background:linear-gradient(160deg,#f4d9cc,#e8b8a6)}
.service-photo--breast{background:linear-gradient(160deg,#f5f3f1,#e6c7b6)}
.service-photo--body{background:linear-gradient(160deg,#e8c1a8,#c98f7a)}
.service-photo--male{background:linear-gradient(160deg,#d9c7b9,#b79a86)}
.service-label{height:40px;line-height:40px;text-align:center;background:var(--pink-soft);color:var(--pink-dark);font-size:15px;font-weight:600;text-transform:uppercase}

/* treatments */
.treatments{height:570px}
.treatments h2{position:absolute;left:40px;top:58px;font-weight:300;font-size:30px;color:var(--pink);text-transform:uppercase;width:1120px;border-bottom:1px solid #e0e0e0;padding-bottom:6px}
.tabs{position:absolute;left:40px;top:132px;display:flex;gap:4px}
.tab{height:40px;line-height:40px;padding:0 26px;background:#3a3a3a;color:var(--white);font-size:12px;font-weight:600;text-transform:uppercase}
.tab.is-active{background:var(--white);color:var(--ink);border:1px solid #dcdcdc;border-bottom:none}
.tab-panel{position:absolute;left:40px;top:172px;width:1120px;height:380px;border:1px solid #dcdcdc;background:var(--white)}
.tab-panel p{position:absolute;left:20px;top:26px;width:540px;font-size:14px;color:var(--muted)}
.price{position:absolute;height:44px;line-height:44px;padding:0 16px;background:#eeeeee;font-size:13px;color:var(--ink)}
.price b{font-weight:700}
.treatment-photo{position:absolute;left:600px;top:26px;width:500px;height:300px;background:linear-gradient(120deg,#c9a594,#ead3c6 50%,#b98a76)}

/* testimonials */
.testimonials{height:490px;background:linear-gradient(90deg,#e4e7ea 0%,#dfe3e6 55%,#c9cfd4 100%)}
.testimonial-photo{position:absolute;right:0;top:0;width:430px;height:490px;background:linear-gradient(180deg,#cfd5da,#b7a193 60%,#d5dadd)}
.testimonials .section-title{padding-top:70px}
.quote{position:absolute;left:100px;top:180px;width:720px;text-align:center}
.quote blockquote{font-style:italic;font-size:22px;color:var(--ink);line-height:1.45}
.quote cite{display:block;font-style:normal;font-size:13px;color:var(--muted);margin-top:22px}
.quote-mark{position:absolute;top:230px;font-size:48px;color:#999;line-height:1}
.testimonial-dots{position:absolute;left:410px;top:390px;display:flex;gap:8px}
.testimonial-dots .dot{background:#c7c7c7}
.testimonial-dots .dot.is-active{background:var(--pink)}

/* blog */
.blog{height:466px;background:var(--pink)}
.blog .section-title{color:var(--white);padding-top:44px}
.posts{position:absolute;left:40px;top:120px;display:flex;gap:40px}
.post{width:346px;background:var(--white)}
.post-photo{height:206px}
.post-photo--guide{background:linear-gradient(160deg,#8fc7e3,#e9cdbd)}
.post-photo--abroad{background:linear-gradient(160deg,#f1ede9,#d9b3a0)}
.post-photo--cost{background:linear-gradient(160deg,#efd7ca,#c7957f)}
.post h3{height:38px;line-height:38px;text-align:center;font-size:13px;font-weight:400;color:var(--ink)}
.blog .btn{position:absolute;left:510px;top:392px;border-color:var(--white);color:var(--white);width:180px;text-align:center}

/* consultation */
.consult{height:267px;background:var(--dark);text-align:center}
.consult .section-title{padding-top:70px}
.consult-row{display:flex;justify-content:center;align-items:center;gap:20px;margin-top:28px;color:var(--white);font-size:20px}
.consult-row .btn{border-color:var(--white);color:var(--white)}

/* footer */
.footer-band{height:103px;background:var(--pink)}
.social{position:absolute;left:40px;top:36px;display:flex;gap:6px}
.social span{width:32px;height:32px;background:var(--pink-dark)}
.signup{position:absolute;right:40px;top:32px;display:flex;align-items:center;gap:14px;color:var(--white);font-size:13px;font-weight:600;text-transform:uppercase}
.signup .field{width:340px;height:40px;background:var(--white);color:#999;font-weight:400;text-transform:none;line-height:40px;padding:0 12px}
.signup .submit{height:40px;line-height:40px;padding:0 26px;background:var(--dark);color:var(--white)}
.copyright{height:44px;background:var(--pink-deep);color:var(--white);font-size:12px;text-align:center;line-height:44px}
.seo-text{height:120px;padding:16px 40px;font-size:11px;color:var(--muted);line-height:1.55}
.seo-text h4{font-size:11px;font-weight:700;color:var(--ink);text-transform:uppercase;margin-bottom:4px}
</style>
</head>
<body>

<header class="site-header">
  <div class="brand">Velora Beauty Clinic</div>
  <div class="appointment"><small>To Schedule a Appointment</small><strong>Call Us: 0800 555 0142</strong></div>
</header>

<nav class="main-nav">
  <ul>
    <li class="is-active">Home</li><li>About Us</li><li>Procedures</li><li>Photo Gallery</li><li>Testimonials</li><li>Financing</li><li>Blog</li><li>Contact Us</li>
  </ul>
</nav>

<section class="hero">
  <div class="hero-photo" role="img" aria-label="Banner photo: woman in a white bikini standing in turquoise sea water"></div>
  <div class="hero-caption">
    <h1>Look Good. Feel Great.</h1>
    <p>Velora Beauty Clinic guarantees excellent results using the top cosmetic surgeon and the most advanced facilities in Cyprus at affordable prices.</p>
    <span class="btn">Learn More</span><span class="btn btn--solid">Schedule a Consultation</span>
  </div>
  <div class="hero-dots"><span class="dot is-active"></span><span class="dot"></span><span class="dot"></span></div>
  <svg class="hero-arrow hero-arrow--prev" viewBox="0 0 44 44"><circle cx="22" cy="22" r="22" fill="#fff"/><path d="M28 14 20 22 28 30" fill="none" stroke="#333" stroke-width="3"/></svg>
  <svg class="hero-arrow hero-arrow--next" viewBox="0 0 44 44"><circle cx="22" cy="22" r="22" fill="#fff"/><path d="M16 14 24 22 16 30" fill="none" stroke="#333" stroke-width="3"/></svg>
</section>

<section class="intro">
  <h2 class="section-title">Face, Body Breast Plastic Surgery</h2>
  <p>Velora Beauty Clinic offers a range of plastic and reconstructive surgery options at affordable prices for those considering medical tourism abroad.</p>
</section>

<section class="experience">
  <div class="doctor-photo" role="img" aria-label="Surgeon in a white coat with a stethoscope, arms crossed"></div>
  <div class="experience-copy">
    <h2>Our Experience Shows</h2>
    <p>If you are considering cosmetic surgery abroad look no further. Plastic surgery abroad is an opportunity to give a desired area of your body a new and improved look. At Velora Beauty Clinic, we promise to deliver the best plastic surgery options and offer outstanding solutions for you and your body. We want to make sure you look the best that you possibly can without compromise.</p>
    <p>Velora Beauty Clinic specialise in facial, breast and body cosmetic and reconstructive surgeries. We have performed plastic surgery for more than 20 years and pride ourselves in achieving very natural looking results. Whatever you need, we can guarantee that you will be delighted with the outcome.</p>
    <span class="btn">Read More About Us</span><span class="btn">Meet Dr. Anselm</span>
  </div>
</section>

<section class="services">
  <h2 class="section-title">What We Do</h2>
  <div class="service-grid">
    <div class="service"><div class="service-photo service-photo--face" role="img" aria-label="Close view of a woman's face"></div><div class="service-label">Face</div></div>
    <div class="service"><div class="service-photo service-photo--breast" role="img" aria-label="Woman in a white bikini top"></div><div class="service-label">Breast</div></div>
    <div class="service"><div class="service-photo service-photo--body" role="img" aria-label="Toned waist and hips in a bikini"></div><div class="service-label">Body</div></div>
    <div class="service"><div class="service-photo service-photo--male" role="img" aria-label="Man's face and shoulders"></div><div class="service-label">Male</div></div>
  </div>
</section>

<section class="treatments">
  <h2>Aesthetic Plastic Surgery Treatments</h2>
  <div class="tabs"><span class="tab is-active">Facial Plastic Surgery</span><span class="tab">Breast Plastic Surgery</span><span class="tab">Body Plastic Surgery</span></div>
  <div class="tab-panel">
    <p>Our facial procedures are planned around you, from a first consultation with the surgeon to your recovery at home. Every treatment uses proven techniques, modern theatres and careful aftercare, so results look natural and last. We explain costs clearly before you book, with no hidden fees and flexible travel dates.</p>
    <div class="price" style="left:20px;top:200px">Eyelid Surgery – <b>From £990</b></div>
    <div class="price" style="left:290px;top:200px">Facelift (incl neck and cheek) – <b>£1900</b></div>
    <div class="price" style="left:20px;top:256px">Rhinoplasty (for functionality) – <b>£1800</b></div>
    <div class="treatment-photo" role="img" aria-label="Two smiling mature women with smooth skin"></div>
  </div>
</section>

<section class="testimonials">
  <div class="testimonial-photo" role="img" aria-label="Woman in a bikini on a beach by the sea"></div>
  <h2 class="section-title" style="width:920px">Cosmetic Surgery Testimonials</h2>
  <span class="quote-mark" style="left:60px">‹</span>
  <span class="quote-mark" style="left:845px">›</span>
  <div class="quote">
    <blockquote>My 2 amazing breasts have arrived! Dr Anselm is amazing and so is his work! Over the moon!!!</blockquote>
    <cite>Procedure: Breast Augmentation – JL – UK – Aug 2014</cite>
  </div>
  <div class="testimonial-dots"><span class="dot"></span><span class="dot is-active"></span><span class="dot"></span><span class="dot"></span></div>
</section>

<section class="blog">
  <h2 class="section-title">Cosmetic Surgery Blog</h2>
  <div class="posts">
    <article class="post"><div class="post-photo post-photo--guide" role="img" aria-label="Woman relaxing by the sea"></div><h3>A Guide To Cosmetic Surgery in Cyprus</h3></article>
    <article class="post"><div class="post-photo post-photo--abroad" role="img" aria-label="Woman wrapped in a white towel"></div><h3>Cosmetic Surgery Abroad</h3></article>
    <article class="post"><div class="post-photo post-photo--cost" role="img" aria-label="Close view of a woman's bust"></div><h3>Cost of Cosmetic Surgery Procedures</h3></article>
  </div>
  <span class="btn">Read All News</span>
</section>

<section class="consult">
  <h2 class="section-title">Ready for a Consultation?</h2>
  <div class="consult-row"><span>Call Us: <b>0800 555 0142</b> or</span><span class="btn">Schedule a Consultation</span></div>
</section>

<footer>
  <div class="footer-band">
    <div class="social"><span></span><span></span><span></span><span></span><span></span><span></span></div>
    <div class="signup"><span>Sign up for monthly coupons</span><span class="field">Enter Email Address</span><span class="submit">Submit</span></div>
  </div>
  <div class="copyright">© 2001-2014 · Velora Beauty Clinic · All rights reserved | Privacy Policy | Terms &amp; Conditions | Sitemap</div>
  <div class="seo-text">
    <h4>Cosmetic Surgery Holiday in Cyprus</h4>
    <p>If you are considering a cosmetic surgery holiday, Velora Beauty Clinic offers a complete package including consultation, surgery, accommodation and airport transfers. Our team looks after every detail so you can relax and recover in a calm setting by the sea. Contact us today to arrange a free first assessment and learn which procedure suits your goals, budget and preferred travel dates.</p>
  </div>
</footer>

</body>
</html>
```